Lanternleaf - Fresh Asian Cuisine Menu

We need to redo our menu to include pictures of food items. Our restaurant is vibrant, trendy, upscale Chinese cuisine

Requirements
Must have
• Must fit on 8.5x11 paper. We can remove the About Us section if needed but menu cannot be more than 6 pages total. Must include pictures of menu items

```html
<!DOCTYPE html>
<html lang="en">
<head>
<meta charset="utf-8">
<title>Lanternleaf - Fresh Asian Cuisine — Entrees</title>
<link rel="stylesheet" href="https://fonts.googleapis.com/css2?family=Nunito+Sans:wght@300;400&family=Nunito:wght@400;800&family=Questrial&display=swap">
<style>
  :root {
    --ink: #ffffff;
    --ink-soft: #f3ece6;
    --bar: #fbf4f1;
    --bg-1: #3a2418;
    --bg-2: #6b4426;
    --bg-3: #22160f;
    --photo-1: #8a4a24;
    --photo-2: #d9c7b4;
  }
  * { box-sizing: border-box; margin: 0; padding: 0; }
  html, body { width: 927px; height: 1200px; overflow: hidden; }
  body { position: relative; color: var(--ink); font-family: "Nunito", sans-serif; }
  .backdrop {
    position: absolute; inset: 0;
    background:
      radial-gradient(ellipse at 70% 35%, rgba(180,120,60,.55), transparent 55%),
      radial-gradient(ellipse at 25% 75%, rgba(150,90,45,.5), transparent 60%),
      radial-gradient(ellipse at 85% 85%, rgba(120,80,50,.5), transparent 55%),
      linear-gradient(160deg, var(--bg-2), var(--bg-1) 50%, var(--bg-3));
  }
  .page-title {
    position: absolute; top: 26px; left: 0; width: 100%;
    text-align: center; font-family: "Nunito Sans", sans-serif; font-weight: 300;
    font-size: 46px; letter-spacing: 1px;
  }
  .section-title {
    position: absolute; left: 27px;
    font-family: "Nunito Sans", sans-serif; font-weight: 300; font-size: 37px;
  }
  .section-bar {
    position: absolute; left: 30px; width: 394px; height: 6px;
    border-radius: 3px; background: var(--bar);
  }
  .item { position: absolute; width: 420px; height: 92px; }
  .item-photo {
    position: absolute; left: 0; top: 0; width: 138px; height: 92px;
    border-radius: 12px;
    background: radial-gradient(circle at 50% 50%, var(--photo-1) 0 32%, var(--photo-2) 34% 44%, #5a4032 46%);
  }
  .item-text { position: absolute; left: 150px; top: 8px; width: 200px; }
  .item-name { font-weight: 800; font-size: 16px; line-height: 1; margin-bottom: 6px; letter-spacing: .2px; }
  .item-desc { font-family: "Questrial", sans-serif; font-size: 13px; line-height: 16.4px; color: var(--ink-soft); }
  .item-desc.small { font-size: 10px; line-height: 13.5px; width: 252px; }
  .item-desc.small .price-gap { float: right; width: 34px; height: 27px; }
  .item-desc.compact { font-size: 11.5px; line-height: 15px; width: 216px; letter-spacing: -.2px; }
  .item-name.two-line { line-height: 15px; margin-bottom: 3px; width: 240px; }
  .item-price {
    position: absolute; left: 370px; top: 0; height: 92px;
    display: flex; align-items: center;
    font-family: "Questrial", sans-serif; font-size: 29px;
  }
</style>
</head>
<body>
  <div class="backdrop" role="img" aria-label="Softly blurred photograph of plated Asian dishes"></div>

  <h1 class="page-title">ENTREES</h1>

  <h2 class="section-title" style="top:140px">CHICKEN</h2>
  <div class="section-bar" style="top:187px"></div>

  <div class="item" style="left:30px;top:220px">
    <div class="item-photo" role="img" aria-label="Kung Pao Chicken with peanuts and chili"></div>
    <div class="item-text"><h3 class="item-name">Kung Pao Chicken</h3><p class="item-desc">Chicken sautéed with roasted peanuts and dry red chili in Kung Pao sauce</p></div>
    <div class="item-price">$13</div>
  </div>
  <div class="item" style="left:30px;top:329px">
    <div class="item-photo" role="img" aria-label="Orange Chicken on a plate with broccoli"></div>
    <div class="item-text" style="top:4px"><h3 class="item-name">Orange Chicken</h3><p class="item-desc">Battered-fried chicken breast with dried chili peppers and stir fried in a tangy orange flavored sauce</p></div>
    <div class="item-price">$13</div>
  </div>
  <div class="item" style="left:30px;top:439px">
    <div class="item-photo" role="img" aria-label="Double Pepper Chicken in red chili broth"></div>
    <div class="item-text" style="top:10px"><h3 class="item-name">Double Pepper Chicken</h3><p class="item-desc">Farm raised chicken with peppercorn, Thai chili,Serrano ,peppers, jalapeños rice noodles,tofu and cilantro</p></div>
    <div class="item-price">$15</div>
  </div>
  <div class="item" style="left:30px;top:551px">
    <div class="item-photo" role="img" aria-label="Crispy Spicy Chicken with peppers"></div>
    <div class="item-text"><h3 class="item-name">Crispy Spicy Chicken</h3><p class="item-desc">Crispy-diced chicken with ,Sichuan peppers, garlic scallions and red and green bell peppers</p></div>
    <div class="item-price">$14</div>
  </div>

  <div class="item" style="left:486px;top:220px">
    <div class="item-photo" role="img" aria-label="General Tso's Chicken with broccoli"></div>
    <div class="item-text"><h3 class="item-name">General Tso’s Chicken</h3><p class="item-desc">Battered-fried chicken breast, stir fried in a sweet &amp; tangy chili sauce with chili peppers</p></div>
    <div class="item-price">$13</div>
  </div>
  <div class="item" style="left:486px;top:329px">
    <div class="item-photo" role="img" aria-label="Shredded chicken in spicy garlic sauce"></div>
    <div class="item-text" style="top:3px"><h3 class="item-name two-line">Shredded Chicken in Spicy Garlic Sauce</h3><p class="item-desc small"><span class="price-gap"></span>Tender shredded chicken, wood ear mushrooms,bamboo shoots, broccoli, green &amp; red bell peppers &amp; Chinese water chestnuts in a classic spicy garlic sauce</p></div>
    <div class="item-price">$14</div>
  </div>
  <div class="item" style="left:486px;top:439px">
    <div class="item-photo" role="img" aria-label="Sweet and Sour Chicken with dipping sauce"></div>
    <div class="item-text" style="top:6px"><h3 class="item-name">Sweet &amp; Sour Chicken</h3><p class="item-desc">Crispy Chicken with green bell peppers, onions and pineapple glazed in a homemade sweet and sour marinade</p></div>
    <div class="item-price">$13</div>
  </div>

  <h2 class="section-title" style="top:714px">SEAFOOD</h2>
  <div class="section-bar" style="top:761px"></div>

  <div class="item" style="left:30px;top:794px">
    <div class="item-photo" role="img" aria-label="Kung Pao Shrimp with peanuts"></div>
    <div class="item-text"><h3 class="item-name">Kung Pao Shrimp</h3><p class="item-desc">Sautéed shrimp with roasted peanuts and dry red chilis in Kung Pao sauce</p></div>
    <div class="item-price">$16</div>
  </div>
  <div class="item" style="left:30px;top:904px">
    <div class="item-photo" role="img" aria-label="Rice Wine Shrimp and Tofu"></div>
    <div class="item-text"><h3 class="item-name">Rice Wine Shrimp &amp; Tofu</h3><p class="item-desc">Shrimp with rice wine mixed with onions, peas and carrot</p></div>
    <div class="item-price">$18</div>
  </div>
  <div class="item" style="left:30px;top:1014px">
    <div class="item-photo" role="img" aria-label="Shrimp in spicy garlic sauce with vegetables"></div>
    <div class="item-text"><h3 class="item-name">Shrimp in Spicy Garlic</h3><p class="item-desc compact">Shrimp sautéed in a spicy garlic sauce with broccoli,red and green bell peppers, bamboo shoots, wood ear mushrooms and Chinese water chestnuts</p></div>
    <div class="item-price">$15</div>
  </div>

  <div class="item" style="left:486px;top:794px">
    <div class="item-photo" role="img" aria-label="Lemon Peel Shrimp on shredded lettuce"></div>
    <div class="item-text"><h3 class="item-name">Lemon Peel Shrimp</h3><p class="item-desc">Shrimp with fresh lemons in a sweet lemon sauce on a bed of shredded lettuce</p></div>
    <div class="item-price">$15</div>
  </div>
  <div class="item" style="left:486px;top:904px">
    <div class="item-photo" role="img" aria-label="Rice Wine Fish with vegetables"></div>
    <div class="item-text" style="top:5px"><h3 class="item-name">Rice Wine Fish</h3><p class="item-desc">White fish filet with rice wine mixed with onions, peas and carrots</p></div>
    <div class="item-price">$14</div>
  </div>
</body>
</html>
```